New Manager Resource Guide & Planner

I need a template designed for a resource guide and planner that new managers would use to help guide them their first year managing others. Think your typical planner injected with tips, worksheets, quotes and other helpful tools. Initially, I'd like a template created for some key pages: one month, one week and single day layouts plus a quote page. I'm attaching a very rudimentary idea of the project, just need it purposefully designed with my colors and branding. The size is 6" x 8 " h. I would like this done in InDesign or Keynote so I can edit it and create other pages. Most likely, though, will contract you to finish out the entire project.

Target Market(s)

new managers (and HR directors who will most likely purchase the resource planner for their employees)

Industry/Entity Type

Advertising

Font styles to use
Other font styles liked:
• archer, open sans

Requirements
Must have
• a creative feel to it (I come from the advertising industry, so a fun design is OK). use of my branding and colors, be noticeably well designed.
Nice to have
• look at other planners for ideas. my goal is to use your template to build out the other pages I need. So think cool edging, or stylized quote boxes, etc.
Should not have
• please use the colors in my palette in the attached pdf plus any other complementary colors you see fit. my branding uses the font archer, open sans, use these and any other fonts that you see fit.

```html
<!DOCTYPE html>
<html lang="en">
<head>
<meta charset="UTF-8">
<title>Week Planer</title>
<link rel="stylesheet" href="https://fonts.googleapis.com/css2?family=Open+Sans:wght@300;400;700&family=Roboto+Slab:wght@100&display=swap">
<style>
  :root {
    --lime: #d4df3f;
    --leaf: #9aab3d;
    --box-line: #dfe6a3;
    --rule: #d8dcc4;
    --dot: #c8c8c8;
    --slate: #76787c;
    --notes-line: #b9babc;
    --paper: #ffffff;
  }
  * { margin: 0; padding: 0; box-sizing: border-box; }
  html, body { width: 1200px; height: 800px; overflow: hidden; background: var(--paper); }
  .planner-page { position: relative; width: 1200px; height: 800px; background: var(--paper); font-family: "Open Sans", sans-serif; }

  .top-band { position: absolute; left: 0; top: 0; width: 1200px; height: 9px; background: var(--lime); }
  .bottom-band { position: absolute; left: 0; top: 771px; width: 1200px; height: 29px; background: var(--lime); }

  .header-rule { position: absolute; left: 28px; height: 1px; background: var(--rule); }
  .header-rule.first { top: 29px; width: 860px; }
  .header-rule.second { top: 48px; width: 866px; }

  .page-title {
    position: absolute; right: 28px; top: 10px;
    font-family: "Roboto Slab", serif; font-weight: 100; font-size: 52px;
    color: var(--leaf); letter-spacing: 0; line-height: 1; white-space: nowrap;
  }

  .day-box { position: absolute; border: 1px solid var(--box-line); background: var(--paper); }
  .day-box.notes { border-color: var(--notes-line); }
  .day-box .title-rule { position: absolute; left: 8px; right: 6px; top: 16px; height: 1px; background: var(--rule); }
  .dot-grid {
    position: absolute; left: 6px; right: 4px; top: 23px; bottom: 4px;
    background-image: radial-gradient(circle, var(--dot) 0.8px, transparent 1.3px);
    background-size: 15.6px 15.5px;
  }

  .day-tab { position: absolute; width: 24px; height: 164px; border: 2px solid var(--leaf); background: var(--paper); overflow: hidden; }
  .day-tab.lime { border-color: var(--lime); }
  .day-tab.slate { border-color: var(--slate); background: var(--slate); }
  .tab-fill { position: absolute; left: 0; right: 0; background: var(--leaf); }
  .day-tab.lime .tab-fill { background: var(--lime); }
  .tab-fill.lower { bottom: 0; top: 56px; }
  .tab-fill.upper { top: 0; height: 104px; }

  .day-label {
    position: absolute; left: 0; width: 20px;
    font-weight: 300; font-size: 14px; letter-spacing: 0.5px; color: var(--paper);
    writing-mode: vertical-rl; line-height: 20px; text-align: left;
  }
  .day-label.rising { bottom: 8px; transform: rotate(180deg); }
  .day-label.falling { top: 8px; }
  .day-label.strong { font-weight: 700; }

  .brand-name {
    position: absolute; right: 28px; top: 771px;
    font-family: "Open Sans", sans-serif; font-weight: 400; font-size: 16px;
    color: var(--paper); line-height: 29px; letter-spacing: 0.3px;
  }
</style>
</head>
<body>
<main class="planner-page">
  <div class="top-band"></div>
  <div class="header-rule first"></div>
  <div class="header-rule second"></div>
  <h1 class="page-title">Week Planer</h1>

  <!-- Monday -->
  <div class="day-tab" style="left:28px; top:70px;"><div class="tab-fill lower"></div><span class="day-label rising">MONDAY</span></div>
  <section class="day-box" style="left:60px; top:70px; width:523px; height:165px;"><div class="title-rule"></div><div class="dot-grid"></div></section>

  <!-- Tuesday -->
  <section class="day-box" style="left:28px; top:246px; width:523px; height:165px;"><div class="title-rule"></div><div class="dot-grid"></div></section>
  <div class="day-tab lime" style="left:559px; top:246px;"><div class="tab-fill upper"></div><span class="day-label falling">TUESDAY</span></div>

  <!-- Wednesday -->
  <div class="day-tab" style="left:28px; top:423px;"><div class="tab-fill lower"></div><span class="day-label rising">WEDNESDAY</span></div>
  <section class="day-box" style="left:60px; top:423px; width:523px; height:165px;"><div class="title-rule"></div><div class="dot-grid"></div></section>

  <!-- Thursday -->
  <section class="day-box" style="left:28px; top:599px; width:523px; height:165px;"><div class="title-rule"></div><div class="dot-grid"></div></section>
  <div class="day-tab lime" style="left:559px; top:599px;"><div class="tab-fill upper"></div><span class="day-label falling">THURSDAY</span></div>

  <!-- Friday -->
  <div class="day-tab" style="left:617px; top:70px;"><div class="tab-fill lower"></div><span class="day-label rising">FRIDAY</span></div>
  <section class="day-box" style="left:648px; top:70px; width:524px; height:165px;"><div class="title-rule"></div><div class="dot-grid"></div></section>

  <!-- Saturday -->
  <section class="day-box" style="left:617px; top:246px; width:523px; height:165px;"><div class="title-rule"></div><div class="dot-grid"></div></section>
  <div class="day-tab lime" style="left:1148px; top:246px;"><div class="tab-fill upper"></div><span class="day-label falling">SATURDAY</span></div>

  <!-- Sunday -->
  <div class="day-tab" style="left:617px; top:423px;"><div class="tab-fill lower"></div><span class="day-label rising">SUNDAY</span></div>
  <section class="day-box" style="left:648px; top:423px; width:524px; height:165px;"><div class="title-rule"></div><div class="dot-grid"></div></section>

  <!-- Notes -->
  <section class="day-box notes" style="left:617px; top:599px; width:523px; height:165px;"><div class="dot-grid" style="top:12px;"></div></section>
  <div class="day-tab slate" style="left:1148px; top:599px;"><span class="day-label falling strong">NOTES</span></div>

  <div class="bottom-band"></div>
  <p class="brand-name">Fieldline Leadership</p>
</main>
</body>
</html>
```